Designing a billboard

Should have
Corwell & Pine, LLC
Ph: 512-647-3918
Auto Accidents / Personal Injury
Family Law
Criminal Defense
Real Estate
Free Consultation

Target Market(s)

Legal

Industry/Entity Type

Legal

Font styles to use
Serif
Sans Serif

Requirements
Must have
• Designing a billboard

Should have
Corwell & Pine, LLC
Ph: 512-647-3918
Family Law
Criminal Defense
Real Estate
Free Consultation
Nice to have
• Nice to have info above
Should not have
• None

```html
<!DOCTYPE html>
<html lang="en">
<head>
<meta charset="utf-8">
<title>Corwell &amp; Pine LLC Billboard</title>
<link href="https://fonts.googleapis.com/css2?family=Libre+Baskerville&family=Open+Sans:wght@700&family=Archivo:wght@800&display=swap" rel="stylesheet">
<style>
  :root {
    --page: #e8eaed;
    --brown: #2c1012;
    --brown-deep: #150809;
    --ink: #000000;
    --white: #ffffff;
    --gavel-light: #6b4a3a;
    --gavel-dark: #1a0b0a;
  }
  html, body {
    margin: 0;
    padding: 0;
    width: 1200px;
    height: 1181px;
    overflow: hidden;
    background: var(--page);
  }
  .billboard {
    position: absolute;
    left: 0;
    top: 400px;
    width: 1200px;
    height: 382px;
    overflow: hidden;
    background: linear-gradient(90deg, var(--brown) 0%, var(--brown) 45%, var(--brown-deep) 100%);
  }
  .gavel-photo {
    position: absolute;
    left: 820px;
    top: 0;
    width: 380px;
    height: 285px;
    background: radial-gradient(ellipse at 62% 40%, var(--gavel-light) 0%, #3a2219 35%, var(--gavel-dark) 70%, rgba(21,8,9,0) 100%);
  }
  .corner-stripes {
    position: absolute;
    left: 0;
    top: 0;
    width: 1200px;
    height: 382px;
  }
  .firm-name {
    position: absolute;
    left: 120px;
    top: 88px;
    margin: 0;
    font-family: "Libre Baskerville", serif;
    font-weight: 400;
    color: var(--white);
    font-size: 70px;
    line-height: 82px;
    letter-spacing: 0;
  }
  .firm-name .suffix { font-size: 46px; }
  .divider {
    position: absolute;
    left: 632px;
    top: 60px;
    width: 4px;
    height: 218px;
    background: var(--white);
  }
  .services {
    position: absolute;
    left: 692px;
    top: 64px;
    margin: 0;
    padding: 0;
    list-style: none;
    font-family: "Open Sans", sans-serif;
    font-weight: 700;
    color: var(--white);
    font-size: 26px;
    letter-spacing: 0.8px;
    line-height: 27px;
  }
  .services li {
    position: relative;
    padding-left: 23px;
    margin-bottom: 11px;
  }
  .services li::before {
    content: "";
    position: absolute;
    left: 0;
    top: 9px;
    width: 11px;
    height: 11px;
    border-radius: 50%;
    background: var(--white);
  }
  .phone-band {
    position: absolute;
    left: 0;
    top: 309px;
    width: 1200px;
    height: 47px;
    background: var(--white);
  }
  .phone-band .bar {
    position: absolute;
    top: 6px;
    height: 36px;
    background: var(--ink);
  }
  .phone-band .bar.left { left: 0; width: 350px; }
  .phone-band .bar.right { left: 848px; width: 352px; }
  .phone-number {
    position: absolute;
    left: 350px;
    top: 0;
    width: 498px;
    height: 47px;
    margin: 0;
    text-align: center;
    font-family: "Archivo", sans-serif;
    font-weight: 800;
    font-size: 50px;
    line-height: 47px;
    color: var(--ink);
    letter-spacing: 1px;
  }
</style>
</head>
<body>
  <section class="billboard">
    <div class="gavel-photo" role="img" aria-label="Photo of a wooden judge's gavel resting on its sound block"></div>

    <svg class="corner-stripes" viewBox="0 0 1200 382" aria-hidden="true">
      <polygon points="0,0 96,0 0,75" fill="#ffffff"/>
      <polygon points="124,0 152,0 0,118 0,96" fill="#ffffff"/>
      <polygon points="1048,0 1080,0 1200,92 1200,117" fill="#ffffff"/>
      <polygon points="1108,0 1200,0 1200,70" fill="#ffffff"/>
    </svg>

    <h1 class="firm-name">CORWELL &amp;<br>PINE <span class="suffix">LLC</span></h1>

    <div class="divider"></div>

    <ul class="services">
      <li>AUTO ACCIDENTS /<br>PERSONAL INJURY</li>
      <li>FAMILY LAW</li>
      <li>CRIMINAL DEFENSE</li>
      <li>REAL ESTATE</li>
      <li>FREE CONSULTATION</li>
    </ul>

    <div class="phone-band">
      <div class="bar left"></div>
      <p class="phone-number">PH: 512-647-3918</p>
      <div class="bar right"></div>
    </div>
  </section>
</body>
</html>
```